Business Card Design

We need a business card designed which uses our logo and looks really good. The company is called Veltramor482. We help e-commerce companies reduce cart abandonment by rescuing the sale through our innovative technology.

Our corporate colors are red, black and white.

I have attached our AI file for the logo as well.

Additional information for the business card:

Name: Marcus Delby
Title: President/CTO
Phone: 1-877-VELT-482
Website: www.veltramor482.com
Email: marcus@veltramor482.com

Tag line: Turning Browsers Into Clients

Industry/Entity Type

E-Commerce

```html
<!DOCTYPE html>
<html lang="en">
<head>
<meta charset="utf-8">
<title>Veltramor482 Business Card</title>
<link href="https://fonts.googleapis.com/css2?family=Open+Sans:wght@400;600&family=Arimo:wght@400&display=swap" rel="stylesheet">
<style>
  :root {
    --backdrop: #e9e7e4;
    --card-dark: #38383a;
    --card-dark-alt: #414143;
    --band-white: #ffffff;
    --ink-dark: #1e1e1e;
    --ink-light: #f4f4f4;
    --ink-muted: #d8d8d8;
    --brand-red: #d2232a;
  }
  * { margin: 0; padding: 0; box-sizing: border-box; }
  html, body {
    width: 1200px;
    height: 800px;
    overflow: hidden;
    background: var(--backdrop);
  }
  .canvas {
    position: relative;
    width: 1200px;
    height: 800px;
  }
  .card {
    position: absolute;
    top: 257px;
    width: 500px;
    height: 286px;
    box-shadow: 0 6px 18px rgba(0,0,0,0.22);
    overflow: hidden;
  }
  /* Front */
  .card-front {
    left: 70px;
    background: var(--card-dark);
    border-radius: 26px 26px 0 0;
  }
  .front-band {
    position: absolute;
    left: 0;
    top: 82px;
    width: 100%;
    height: 66px;
    background: var(--band-white);
    display: flex;
    align-items: center;
    justify-content: center;
  }
  .front-wordmark {
    font-family: "Open Sans", sans-serif;
    font-weight: 600;
    font-size: 44px;
    letter-spacing: 1px;
    color: var(--ink-dark);
  }
  .front-tagline {
    position: absolute;
    left: 0;
    top: 186px;
    width: 100%;
    text-align: center;
    font-family: "Open Sans", sans-serif;
    font-size: 19px;
    color: var(--ink-light);
  }
  /* Back */
  .card-back {
    left: 630px;
    background: linear-gradient(160deg, var(--card-dark-alt), var(--card-dark));
    border-radius: 0 30px 0 0;
  }
  .back-wordmark {
    position: absolute;
    left: 30px;
    top: 94px;
    font-family: "Open Sans", sans-serif;
    font-weight: 600;
    font-size: 20px;
    letter-spacing: 0.5px;
    color: var(--ink-light);
  }
  .back-rule {
    position: absolute;
    left: 62px;
    top: 128px;
    width: 438px;
    height: 2px;
    background: var(--brand-red);
  }
  .contact-name {
    position: absolute;
    right: 22px;
    top: 98px;
    font-family: "Arimo", sans-serif;
    font-size: 19px;
    color: var(--ink-light);
  }
  .contact-title {
    position: absolute;
    right: 40px;
    top: 135px;
    font-family: "Arimo", sans-serif;
    font-size: 10px;
    color: var(--ink-muted);
  }
  .contact-list {
    position: absolute;
    left: 190px;
    top: 196px;
    font-family: "Arimo", sans-serif;
    font-size: 12px;
    line-height: 16px;
    color: var(--ink-light);
    border-collapse: collapse;
  }
  .contact-list td { padding: 0; }
  .contact-list .contact-label { padding-right: 6px; }
</style>
</head>
<body>
<main class="canvas">
  <section class="card card-front" aria-label="Business card front">
    <div class="front-band">
      <span class="front-wordmark">Veltramor482</span>
    </div>
    <p class="front-tagline">Turning Browsers Into Clients</p>
  </section>

  <section class="card card-back" aria-label="Business card back">
    <span class="back-wordmark">Veltramor482</span>
    <div class="back-rule"></div>
    <p class="contact-name">Marcus Delby</p>
    <p class="contact-title">President/CTO</p>
    <table class="contact-list">
      <tr><td class="contact-label">phone</td><td>: 1-877-VELT-482</td></tr>
      <tr><td class="contact-label">website</td><td>: www.veltramor482.com</td></tr>
      <tr><td class="contact-label">email</td><td>: marcus@veltramor482.com</td></tr>
    </table>
  </section>
</main>
</body>
</html>
```